Asia based real estate financing firm needs and AWESOME design for a biz card -Harbor Lending Circle

Looking for a stylish, & corporate-looking business card for a real estate financing brokerage firm in Asia, offering global mortgage loans. I uploaded our current logos. We would like to add a splash of color (perhaps the house icon) or any other suggestions are open. For the winning designer, we have a lot of work! Thanks and best of luck!

Target Market(s)

Real estate investors globally. We want to look more like a BANK and NOT a real estate company. Please don't play up on a "house" design.

Industry/Entity Type

Banking

Contact Information for Business Card

Harbor Lending Circle
Peter Wilks
Co-Founder | Partner

14 Cassia Lane, Suite 310
Singapore 047219
www.hlc-example.asia
peterwilks@hlc-example.asia
+65 555-0142
WeChat: peterwilks

Colors

Designer to choose colors to be used in the design.

Requirements
Must have
• Must have the standard business requirements for a card; name, address, email, etc
• Can be horizontal or vertical.
Nice to have
• It would be great to see some sort of variation to the logo with a pop of color. Red is good as we're in Asia, however, other options work as well.
• Our tag line is - Lending without limits. It doesn't have to be on the card but might be nice.
• I'd like to start seeing our tagline within the cards as well. - Lending without limits.
• Also, please add our location. The location for this card is Singapore so perhaps it can be highlighted or emphasised in some way.
• Singapore | Hong Kong | Shanghai | Manila
• As we will soon open an office in Shanghai, having an option for both languages would be great.
Should not have
• I'm exceited and open to your creativity ... knock it out of the park!

```html
<!DOCTYPE html>
<html lang="en">
<head>
<meta charset="utf-8">
<title>Harbor Lending Circle — Business Card</title>
<link href="https://fonts.googleapis.com/css2?family=Cinzel:wght@400&family=Open+Sans:wght@400;700&display=swap" rel="stylesheet">
<style>
  :root {
    --backdrop: #2b2b2b;
    --card: #ffffff;
    --ink: #111111;
    --muted: #6d6d6d;
    --soft: #8a8a8a;
  }
  * { margin: 0; padding: 0; box-sizing: border-box; }
  html, body { width: 1200px; height: 892px; overflow: hidden; }
  body {
    background: var(--backdrop);
    font-family: "Open Sans", Arial, sans-serif;
    color: var(--ink);
    position: relative;
  }
  .card {
    position: absolute;
    width: 560px;
    height: 320px;
    background: var(--card);
    box-shadow: 0 10px 30px rgba(0,0,0,.45);
  }
  .card--front { left: 90px; top: 80px; }
  .card--back { left: 550px; top: 490px; }

  .wordmark {
    font-family: "Cinzel", "Times New Roman", serif;
    font-weight: 400;
    color: var(--ink);
    letter-spacing: .04em;
    line-height: 1.15;
    white-space: nowrap;
  }
  .card--front .wordmark {
    position: absolute;
    left: 0; right: 0; top: 108px;
    text-align: center;
    font-size: 30px;
  }
  .tagline {
    position: absolute;
    left: 0; right: 0; top: 220px;
    text-align: center;
    font-size: 13px;
    letter-spacing: .28em;
    color: var(--soft);
  }

  .card--back .wordmark {
    position: absolute;
    left: 36px; top: 44px;
    font-size: 20px;
  }
  .contact {
    position: absolute;
    left: 36px; top: 106px;
    font-size: 12px;
    color: var(--muted);
    line-height: 1.4;
  }
  .contact__name {
    font-weight: 700;
    font-size: 17px;
    color: var(--ink);
    letter-spacing: .02em;
  }
  .contact__role { margin-bottom: 8px; }
  .contact__address { margin-bottom: 6px; }
  .contact__list { list-style: none; }
  .contact__list li { display: flex; align-items: center; gap: 8px; height: 18px; }
  .contact__list svg { width: 12px; height: 12px; flex: none; }
  .accent-square {
    position: absolute;
    right: 40px; top: 40px;
    width: 170px; height: 170px;
    background: var(--ink);
  }
</style>
</head>
<body>
  <section class="card card--front">
    <div class="wordmark">Harbor Lending Circle</div>
    <p class="tagline">Lending without limits.</p>
  </section>

  <section class="card card--back">
    <div class="wordmark">Harbor Lending Circle</div>
    <div class="contact">
      <div class="contact__name">PETER WILKS</div>
      <div class="contact__role">Co-Founder | Partner</div>
      <div class="contact__address">14 Cassia Lane, Suite 310<br>Singapore 047219</div>
      <ul class="contact__list">
        <li>
          <svg viewBox="0 0 12 12"><path d="M2.5 1l2 2-1 1.3c.6 1.4 1.8 2.6 3.2 3.2L8 6.5l2 2-1.2 1.7C5 10 2 7 1.8 3.2z" fill="#111"/></svg>
          +65 555-0142
        </li>
        <li>
          <svg viewBox="0 0 12 12"><rect x="1" y="2.5" width="10" height="7" fill="#111"/><path d="M1 2.5l5 4 5-4" stroke="#fff" fill="none"/></svg>
          peterwilks@hlc-example.asia
        </li>
        <li>
          <svg viewBox="0 0 12 12"><circle cx="6" cy="6" r="5" fill="#111"/><path d="M1 6h10M6 1c2 2 2 8 0 10M6 1c-2 2-2 8 0 10" stroke="#fff" stroke-width=".7" fill="none"/></svg>
          www.hlc-example.asia
        </li>
        <li>
          <svg viewBox="0 0 12 12"><circle cx="6" cy="6" r="5" fill="#111"/></svg>
          peterwilks
        </li>
      </ul>
    </div>
    <div class="accent-square" aria-hidden="true"></div>
  </section>
</body>
</html>
```